Velvet Dare Age Verification Landing Page

To create a visually appealing design for the landing page of the adult game "Velvet Dare" that confirms the visitor's age.
The design should have a simple and visually appealing look that focuses on two buttons labeled "Yes" and "No". The purpose of the page is to confirm that the visitor is 18 years of age or older before accessing the game's content. Responsive design that works well on desktop and mobile devices. The final output should be delivered in PSD, AI, or Sketch format, along with any necessary images or assets.
I have also attached examples.

```html
<!DOCTYPE html>
<html lang="en">
<head>
<meta charset="utf-8">
<title>Velvet Dare – Age Verification</title>
<link href="https://fonts.googleapis.com/css2?family=Hind:wght@500;600&display=swap" rel="stylesheet">
<style>
  :root {
    --backdrop-dark: #1b2830;
    --backdrop-mid: #34454f;
    --backdrop-warm: #4a4a44;
    --panel: #ffffff;
    --ink: #111111;
    --brand: #cc0e5c;
    --brand-soft: #fbe3ee;
    --on-brand: #ffffff;
  }
  * { box-sizing: border-box; margin: 0; padding: 0; }
  html, body { width: 1200px; height: 547px; overflow: hidden; }
  body {
    position: relative;
    font-family: "Hind", Arial, sans-serif;
    color: var(--ink);
  }
  .backdrop {
    position: absolute;
    inset: 0;
    background:
      radial-gradient(ellipse 260px 200px at 880px 330px, rgba(110,100,80,0.45), transparent 70%),
      radial-gradient(ellipse 300px 260px at 420px 150px, rgba(90,85,70,0.35), transparent 70%),
      linear-gradient(180deg, var(--backdrop-mid) 0%, var(--backdrop-dark) 100%);
  }
  .age-gate {
    position: absolute;
    left: 334px;
    top: 95px;
    width: 532px;
    height: 356px;
    background: var(--panel);
    border-radius: 10px;
    text-align: center;
  }
  .brand-mark {
    position: absolute;
    left: 214px;
    top: 29px;
    width: 104px;
    height: 104px;
    border: 1px solid var(--brand);
    border-radius: 50%;
  }
  .brand-name {
    position: absolute;
    left: 0;
    right: 0;
    top: 146px;
    font-size: 40px;
    font-weight: 600;
    line-height: 1;
    color: var(--ink);
  }
  .question {
    position: absolute;
    left: 0;
    right: 0;
    top: 225px;
    font-size: 18px;
    font-weight: 500;
  }
  .answers {
    position: absolute;
    left: 206px;
    top: 261px;
    display: flex;
    gap: 10px;
  }
  .answer {
    width: 54px;
    height: 42px;
    border: 0;
    background: var(--brand);
    color: var(--on-brand);
    font-family: "Hind", Arial, sans-serif;
    font-size: 18px;
    font-weight: 500;
    padding-top: 3px;
  }
  .remember {
    position: absolute;
    left: 212px;
    top: 315px;
    display: flex;
    align-items: center;
    gap: 10px;
    font-size: 13px;
    font-weight: 500;
  }
  .remember-box {
    width: 9px;
    height: 9px;
    background: var(--brand-soft);
  }
</style>
</head>
<body>
  <div class="backdrop" role="img" aria-label="Blurred background photo of a dimly lit room"></div>
  <main class="age-gate">
    <div class="brand-mark"></div>
    <div class="brand-name">Velvet Dare</div>
    <p class="question">Are You Over 18 years of Age?</p>
    <div class="answers">
      <button class="answer">Yes</button>
      <button class="answer">No</button>
    </div>
    <label class="remember"><span class="remember-box"></span>Remember Me</label>
  </main>
</body>
</html>
```